Business Card design for an International Import Export House

We need a Business Card design for our import export business. We trade in Minerals, Metals, Rice, Sugar, Steel etc.. The design should be minimalistic. It may or may not contain the physical address. In case you want to include the physical address - 418 Verandah Heights, Marlow Sector 9, Kestrel Vale, Norland, India, 560417.

Target Market(s)

Steel Mills or Steel Plants, Factories, Mining businesses, Industrial houses, Government Agencies

Industry/Entity Type

Importer

Contact Information for Business Card

Business Name - Varnell Overseas

Font styles to use
Other font styles liked:
• montserrat

Requirements
Must have
• Ravi Kandola - President
• www.varnelloverseas.com
• ravi@varnelloverseas.com
• +91-987-654-3217
Nice to have
• worldwide suppliers of ores

```html
<!DOCTYPE html>
<html lang="en">
<head>
<meta charset="utf-8">
<title>Varnell Overseas – Business Card</title>
<link rel="stylesheet" href="https://fonts.googleapis.com/css2?family=Montserrat:wght@400;500;600;700&display=swap">
<style>
  :root {
    --backdrop: #2c2a2b;
    --card-white: #ffffff;
    --teal: #3d8ea3;
    --teal-deep: #37869a;
    --teal-bright: #4ba7bd;
    --ink-grey: #6b6b6e;
    --role-tint: #e3f1f5;
  }
  html, body {
    margin: 0;
    padding: 0;
    width: 1200px;
    height: 1000px;
    overflow: hidden;
    background: var(--backdrop);
    font-family: "Montserrat", sans-serif;
  }
  .canvas {
    position: relative;
    width: 1200px;
    height: 1000px;
  }
  .card {
    position: absolute;
    left: 302px;
    width: 652px;
    height: 372px;
    border-radius: 14px;
    overflow: hidden;
    background: var(--card-white);
  }
  .card-front { top: 96px; }
  .card-back { top: 544px; }

  .pattern-area {
    position: absolute;
    left: 0;
    top: 0;
  }

  /* Front */
  .front-brand {
    position: absolute;
    left: 52px;
    top: 306px;
    display: flex;
    align-items: center;
    gap: 10px;
  }
  .brand-dot {
    width: 18px;
    height: 18px;
    border-radius: 50%;
    background: var(--teal);
  }
  .front-brand-name {
    font-size: 20px;
    font-weight: 700;
    color: var(--teal);
    letter-spacing: -0.2px;
    text-transform: uppercase;
    white-space: nowrap;
  }

  /* Back */
  .back-band {
    position: absolute;
    left: 0;
    top: 0;
    width: 652px;
    height: 256px;
    background: linear-gradient(90deg, var(--teal-deep) 0%, var(--teal) 45%, var(--teal-bright) 100%);
  }
  .back-brand {
    position: absolute;
    right: 34px;
    top: 74px;
    display: flex;
    align-items: center;
    gap: 5px;
  }
  .back-brand .brand-dot {
    width: 9px;
    height: 9px;
    background: var(--card-white);
  }
  .back-brand-name {
    font-size: 8px;
    font-weight: 700;
    color: var(--card-white);
    text-transform: uppercase;
    white-space: nowrap;
  }
  .holder {
    position: absolute;
    left: 436px;
    top: 173px;
    color: var(--card-white);
  }
  .holder-name {
    font-size: 21px;
    font-weight: 500;
    text-transform: uppercase;
    letter-spacing: 0.2px;
    line-height: 1;
    white-space: nowrap;
  }
  .holder-role {
    margin-top: 8px;
    font-size: 15px;
    font-weight: 500;
    color: var(--role-tint);
    line-height: 1;
  }
  .contact {
    position: absolute;
    left: 0;
    top: 256px;
    width: 652px;
    height: 116px;
    color: var(--ink-grey);
    text-align: center;
  }
  .contact-line {
    display: flex;
    justify-content: center;
    align-items: center;
    gap: 6px;
    white-space: nowrap;
  }
  .contact-phone { margin-top: 15px; font-size: 17px; font-weight: 500; }
  .contact-online { margin-top: 11px; font-size: 16px; font-weight: 500; }
  .contact-address { margin-top: 9px; font-size: 13.5px; font-weight: 600; }
  .divider { margin: 0 16px; }
  .icon { fill: var(--ink-grey); flex: none; }
</style>
</head>
<body>
<main class="canvas">

  <section class="card card-front" aria-label="Business card front">
    <svg class="pattern-area" width="652" height="372" viewBox="0 0 652 372" role="img" aria-label="Geometric pattern of striped and dotted triangles">
      <defs>
        <linearGradient id="frontPatternTone" x1="0" y1="1" x2="1" y2="0">
          <stop offset="0" stop-color="#e6eaec"/>
          <stop offset="0.5" stop-color="#b9d9e2"/>
          <stop offset="1" stop-color="#6fb0c2"/>
        </linearGradient>
      </defs>
      <polygon points="270,0 652,0 652,258 580,318 355,365 230,145" fill="url(#frontPatternTone)"/>
    </svg>
    <div class="front-brand">
      <span class="brand-dot"></span>
      <span class="front-brand-name">Varnell Overseas</span>
    </div>
  </section>

  <section class="card card-back" aria-label="Business card back">
    <div class="back-band"></div>
    <svg class="pattern-area" width="652" height="256" viewBox="0 0 652 256" role="img" aria-label="Geometric pattern of striped and dotted triangles">
      <defs>
        <linearGradient id="backPatternTone" x1="0" y1="0" x2="1" y2="1">
          <stop offset="0" stop-color="#6fb3c4"/>
          <stop offset="1" stop-color="#3e8ea3"/>
        </linearGradient>
      </defs>
      <polygon points="0,0 430,0 365,70 250,256 0,256" fill="url(#backPatternTone)"/>
    </svg>
    <div class="back-brand">
      <span class="brand-dot"></span>
      <span class="back-brand-name">Varnell Overseas</span>
    </div>
    <div class="holder">
      <div class="holder-name">Ravi Kandola</div>
      <div class="holder-role">President</div>
    </div>

    <div class="contact">
      <div class="contact-line contact-phone">
        <svg class="icon" width="12" height="13" viewBox="0 0 24 24" aria-hidden="true"><path d="M6.6 10.8a15.1 15.1 0 0 0 6.6 6.6l2.2-2.2a1 1 0 0 1 1-.25 11.4 11.4 0 0 0 3.6.57 1 1 0 0 1 1 1V20a1 1 0 0 1-1 1A17 17 0 0 1 3 4a1 1 0 0 1 1-1h3.5a1 1 0 0 1 1 1c0 1.25.2 2.45.57 3.57a1 1 0 0 1-.25 1z"/></svg>
        <span>+91-987-654-3217</span>
      </div>
      <div class="contact-line contact-online">
        <svg class="icon" width="14" height="10" viewBox="0 0 24 17" aria-hidden="true"><path d="M0 0h24v17H0z M2 2v1l10 7 10-7V2z" fill-rule="evenodd"/></svg>
        <span>ravi@varnelloverseas.com</span>
        <span class="divider">|</span>
        <svg class="icon" width="10" height="13" viewBox="0 0 16 22" aria-hidden="true"><path d="M1 1l14 10-6 1 4 8-2.5 1-4-8L1 17z"/></svg>
        <span>www.varnelloverseas.com</span>
      </div>
      <div class="contact-line contact-address">
        <svg class="icon" width="12" height="16" viewBox="0 0 24 32" aria-hidden="true"><path d="M12 0a11 11 0 0 0-11 11c0 8 11 21 11 21s11-13 11-21A11 11 0 0 0 12 0zm0 15a4 4 0 1 1 0-8 4 4 0 0 1 0 8z"/></svg>
        <span>418 Verandah Heights, Marlow Sector 9, Kestrel Vale, Norland, India, 560417.</span>
      </div>
    </div>
  </section>

</main>
</body>
</html>
```